Tavelin Global Kft. is an online recruitment marketplace connecting the employers and recruiters together. We provide an e-bussiness solution for companies and give busines opportunity for recruiters.
We have a logo design already, which should be used on the business card.
Our colours are grey and magenta, which can be seen in the logo. Black is also welcome.
The style should be dynamic, young but professional. It should be clear, visible, elegant, not too crowded, simple but exciting.
We need the following data on the BC: name, title, address, phone,fax and mobile number, email address, website.
Target Market(s)
Our target market are companies, as this is a B2B business. We also target recruiters, recruitment professionals, headhunters.We would like to be impressive and different.
Industry/Entity Type
Business
Requirements
Must have
- We would like to promote our website, www.tavelglob.hu.
- Please, put this on the back with a quite visible letter size.The style should be dynamic, young but professional. It should be clear, visible, elegant, not too crowded, simple but exciting.
Should not have
- We do not want to see people figures.

```html
<!DOCTYPE html>
<html lang="en">
<head>
<meta charset="utf-8">
<title>Tavelin Global Kft. – Business Card</title>
<link rel="stylesheet" href="https://fonts.googleapis.com/css2?family=Noto+Serif:wght@700&family=Arimo:wght@700&display=swap">
<style>
  :root {
    --magenta: #b0186e;
    --grey: #8a7a86;
    --ink: #1c1c1c;
    --paper: #ffffff;
    --backdrop: #e4e4e4;
    --edge: #d2d2d2;
  }
  * { margin: 0; padding: 0; box-sizing: border-box; }
  html, body { width: 1200px; height: 900px; overflow: hidden; }
  body {
    background: var(--backdrop);
    position: relative;
    font-family: "Noto Serif", Georgia, serif;
  }
  .card {
    position: absolute;
    width: 572px;
    height: 324px;
    background: var(--paper);
    border: 1px solid var(--edge);
    overflow: hidden;
  }
  .card--front { left: 306px; top: 52px; }
  .card--back  { left: 306px; top: 512px; }

  /* front */
  .brand-mark {
    position: absolute;
    left: 44px;
    top: 70px;
    width: 170px;
    height: 170px;
    background: var(--magenta);
  }
  .brand-name {
    position: absolute;
    left: 250px;
    top: 82px;
    font-weight: 700;
    font-size: 66px;
    line-height: 1;
    letter-spacing: 1px;
    color: var(--magenta);
  }

  /* back */
  .job-title {
    position: absolute;
    left: 28px;
    top: 8px;
    font-weight: 700;
    font-size: 66px;
    line-height: 1.2;
    color: var(--magenta);
  }
  .contact-labels {
    position: absolute;
    left: 0;
    top: 100px;
    width: 124px;
    list-style: none;
    text-align: right;
    font-family: "Arimo", Arial, sans-serif;
    font-weight: 700;
    font-size: 17px;
    line-height: 28.5px;
    color: var(--ink);
  }
  .brand-lockup {
    position: absolute;
    left: 356px;
    top: 204px;
    display: flex;
    align-items: center;
    gap: 10px;
  }
  .brand-lockup__mark {
    width: 64px;
    height: 64px;
    background: var(--magenta);
  }
  .brand-lockup__name {
    font-weight: 700;
    font-size: 23px;
    line-height: 1.05;
    color: var(--magenta);
  }
</style>
</head>
<body>
  <section class="card card--front" aria-label="Business card front">
    <div class="brand-mark"></div>
    <div class="brand-name">TAVELIN<br>GLOBAL</div>
  </section>

  <section class="card card--back" aria-label="Business card back">
    <h1 class="job-title">manager</h1>
    <ul class="contact-labels">
      <li>NAME</li>
      <li>ADDRESS</li>
      <li>PHONE</li>
      <li>FAX</li>
      <li>MOBILE</li>
      <li>EMAIL</li>
      <li>WEBSITE</li>
    </ul>
    <div class="brand-lockup">
      <div class="brand-lockup__mark"></div>
      <div class="brand-lockup__name">TAVELIN<br>GLOBAL</div>
    </div>
  </section>
</body>
</html>
```